You are cordially invited to attend a delicious Afternoon Tea at The Harcourt.

Enjoy a glass of sparkling wine whilst afternoon delicacies and a menu of fine teas is presented for you to enjoy throughout the afternoon.

This is an opportunity to get together with a table of like minded ladies just for fun and to share some stories and meet some new friends.

Date: 8 August 2014
Time: 12pm - 2pm
Venue: 48 Larkmoor Lane, Melbourne VIC 3000

(hello please see above text we require - we would like to invite our clients to an afternoon tea, an invitation (hard copy) to be of elegant taste, nice lettering, pic added to the invite).

```html
<!DOCTYPE html>
<html lang="en">
<head>
<meta charset="UTF-8">
<title>Afternoon Tea Invitation – The Harcourt</title>
<link rel="stylesheet" href="https://fonts.googleapis.com/css2?family=Josefin+Sans:wght@600;700&family=Dosis:wght@300;400&display=swap">
<style>
  :root {
    --page-bg: #d9d9d9;
    --card-black: #050304;
    --card-wine: #5a0a22;
    --glow-crimson: #c4164c;
    --title-pink: #ec1c5c;
    --lead-text: #e9bccb;
    --body-text: #d8789a;
    --details-text: #eadde1;
    --photo-rose: #c9a9b1;
    --photo-mauve: #8e6f78;
  }
  * { margin: 0; padding: 0; box-sizing: border-box; }
  html, body { width: 1200px; height: 1000px; overflow: hidden; }
  body {
    background: var(--page-bg);
    position: relative;
    font-family: "Dosis", sans-serif;
  }
  .invitation-card {
    position: absolute;
    left: 50px;
    top: 142px;
    width: 1100px;
    height: 715px;
    overflow: hidden;
    background:
      radial-gradient(ellipse 520px 600px at 0% 50%, rgba(196,22,76,0.55), rgba(90,10,34,0.35) 45%, transparent 80%),
      linear-gradient(160deg, #1e0208 0%, var(--card-black) 55%);
  }
  .wine-photo {
    position: absolute;
    left: 0;
    top: 0;
    width: 480px;
    height: 715px;
    background: linear-gradient(90deg, rgba(196,22,76,0.75) 0%, rgba(150,14,56,0.55) 35%, rgba(60,6,22,0.25) 75%, transparent 100%);
  }
  .invitation-title {
    position: absolute;
    left: 300px;
    width: 750px;
    top: 62px;
    text-align: center;
    font-family: "Josefin Sans", sans-serif;
    font-weight: 700;
    font-size: 58px;
    letter-spacing: 4px;
    color: var(--title-pink);
  }
  .invitation-copy {
    position: absolute;
    left: 300px;
    width: 750px;
    top: 186px;
    text-align: center;
    font-weight: 300;
  }
  .lead {
    font-size: 18px;
    line-height: 25px;
    color: var(--lead-text);
    font-weight: 400;
  }
  .body {
    margin-top: 22px;
    font-size: 14px;
    line-height: 21px;
    color: var(--body-text);
  }
  .event-details {
    position: absolute;
    left: 300px;
    width: 750px;
    top: 412px;
    text-align: center;
    font-size: 18px;
    color: var(--details-text);
    font-weight: 400;
    white-space: nowrap;
  }
  .event-details .divider { margin: 0 18px; }
  .venue-photo {
    position: absolute;
    left: 289px;
    top: 454px;
    width: 811px;
    height: 261px;
    border-top-left-radius: 26px;
    background: linear-gradient(90deg, rgba(201,169,177,0.55) 0%, var(--photo-rose) 30%, var(--photo-mauve) 100%);
  }
</style>
</head>
<body>
  <main class="invitation-card">
    <div class="wine-photo" role="img" aria-label="Photo of a red wine bottle and a half-filled wine glass against a crimson backdrop"></div>

    <h1 class="invitation-title">INVITATION</h1>

    <section class="invitation-copy">
      <p class="lead">You are cordially invited<br>to attend a delicious Afternoon Tea at The Harcourt.</p>
      <p class="body">Enjoy a glass of sparkling wine whilst afternoon delicacies<br>and a menu of fine teas is presented for you to enjoy throughout the afternoon.</p>
      <p class="body">This is an opportunity to get together<br>with a table of like minded ladies just for fun and to share some stories and meet some new friends.</p>
    </section>

    <p class="event-details">
      <span>Date: 8 August 2014</span><span class="divider">|</span><span>Time: 12pm - 2pm</span><span class="divider">|</span><span>Venue: 48 Larkmoor Lane, Melbourne VIC 3000</span>
    </p>

    <div class="venue-photo" role="img" aria-label="Photo of an elegant tea room table set with a tiered cake stand, teacups and upholstered chairs"></div>
  </main>
</body>
</html>
```